App Company Business Card Design Project

We are looking for a two sided business card design with one side in English and one side in Chinese. Information should include:
1. Name
2. Email
3. Cell phone
4. Address
Please incorporate the logo attached. Above are the only requirements.

Industry/Entity Type

Business

```html
<!DOCTYPE html>
<html lang="en">
<head>
<meta charset="utf-8">
<title>Halcyon Spring – Business Card</title>
<link href="https://fonts.googleapis.com/css2?family=Open+Sans:wght@400;600;700&display=swap" rel="stylesheet">
<style>
  :root {
    --page-bg: #ececec;
    --card-bg: #ffffff;
    --ink: #555555;
    --ink-strong: #4a4a4a;
    --rule: #6b6b6b;
    --green: #3dba5a;
    --cyan: #1cb5d4;
    --orange: #f28c45;
  }
  * { margin: 0; padding: 0; box-sizing: border-box; }
  html, body {
    width: 1200px;
    height: 1000px;
    overflow: hidden;
    background: var(--page-bg);
    font-family: "Open Sans", Arial, sans-serif;
  }
  .card {
    position: absolute;
    left: 150px;
    top: 236px;
    width: 900px;
    height: 528px;
    background: var(--card-bg);
    box-shadow: 0 10px 30px rgba(0,0,0,0.18);
  }
  .brand {
    position: absolute;
    left: 59px;
    top: 248px;
    display: flex;
    align-items: center;
    gap: 24px;
  }
  .brand-dot {
    width: 42px;
    height: 42px;
    border-radius: 50%;
    background: var(--cyan);
    flex: none;
  }
  .brand-name {
    font-size: 30px;
    font-weight: 600;
    letter-spacing: 3px;
    color: var(--ink);
    white-space: nowrap;
  }
  .divider {
    position: absolute;
    left: 450px;
    top: 136px;
    width: 2px;
    height: 256px;
    background: var(--rule);
  }
  .holder-name {
    position: absolute;
    left: 472px;
    top: 148px;
    font-size: 32px;
    font-weight: 700;
    color: var(--ink-strong);
    letter-spacing: 1px;
  }
  .contact-list {
    position: absolute;
    left: 466px;
    top: 210px;
    list-style: none;
  }
  .contact-item {
    display: flex;
    align-items: center;
    height: 46px;
    margin-bottom: 14px;
  }
  .contact-item:last-child { margin-top: 6px; }
  .contact-icon {
    width: 46px;
    height: 46px;
    flex: none;
  }
  .contact-text {
    margin-left: 13px;
    font-size: 23px;
    color: var(--ink);
    white-space: nowrap;
  }
</style>
</head>
<body>
  <main class="card">
    <div class="brand">
      <span class="brand-dot"></span>
      <span class="brand-name">HALCYON SPRING</span>
    </div>

    <div class="divider"></div>

    <h1 class="holder-name">NAME</h1>

    <ul class="contact-list">
      <li class="contact-item">
        <svg class="contact-icon" viewBox="0 0 46 46" aria-hidden="true">
          <circle cx="23" cy="23" r="23" fill="var(--green)"/>
          <rect x="12" y="15" width="24" height="16" rx="1.5" fill="#fff"/>
          <path d="M12 16 L24 25 L36 16" fill="none" stroke="var(--green)" stroke-width="2"/>
        </svg>
        <span class="contact-text">email@email.com</span>
      </li>
      <li class="contact-item">
        <svg class="contact-icon" viewBox="0 0 46 46" aria-hidden="true">
          <circle cx="23" cy="23" r="23" fill="var(--cyan)"/>
          <path d="M12 17 Q23 9 34 17 L31 21 L27 19 L19 19 L15 21 Z" fill="#fff"/>
          <rect x="14" y="22" width="18" height="12" rx="2" fill="#fff"/>
          <g fill="var(--cyan)">
            <rect x="17" y="25" width="3" height="2"/><rect x="21.5" y="25" width="3" height="2"/><rect x="26" y="25" width="3" height="2"/>
            <rect x="17" y="29" width="3" height="2"/><rect x="21.5" y="29" width="3" height="2"/><rect x="26" y="29" width="3" height="2"/>
          </g>
        </svg>
        <span class="contact-text">+370 600 41275</span>
      </li>
      <li class="contact-item">
        <svg class="contact-icon" viewBox="0 0 46 46" aria-hidden="true">
          <circle cx="23" cy="23" r="23" fill="var(--orange)"/>
          <path d="M9 24 L23 12 L37 24" fill="none" stroke="#fff" stroke-width="3.5" stroke-linejoin="round"/>
          <rect x="18" y="27" width="10" height="10" fill="#fff"/>
        </svg>
        <span class="contact-text">Address str. 05202 Adress</span>
      </li>
    </ul>
  </main>
</body>
</html>
```